cryotherapy business . Whole Body Cryotherapy, Localised Cryotherapy, Cryofacials

Need home page plus services, about, pricing, online booking, contact and blog page

I want something slick, hip and professional. Our studio colours are duck egg blue, white and grey

I would also like a social media scroll at the bottom of every page

I will upload some web designs that I like the look of

Target Market(s)

Men and Women 25-45

Industry/Entity Type

Health And Wellness

Coding

Coded - Design and coding required

Number of Pages Required

5+ page

Font styles to use
Serif
Sans Serif

Requirements
Must have
• Must be eye catching and easy to navigate
Nice to have
• animation
Should not have
• Not sure what the site should not have. I am fairly open to ideas as this is a brand new business.

```html
<!DOCTYPE html>
<html lang="en">
<head>
<meta charset="utf-8">
<title>Frostwell – Cryotherapy Studio</title>
<link href="https://fonts.googleapis.com/css2?family=Raleway:wght@300;400;500;600&family=Open+Sans:wght@400;600&display=swap" rel="stylesheet">
<style>
  :root{
    --hero-deep:#123f93;
    --hero-mid:#2a6fcb;
    --hero-light:#9cc3ea;
    --duck-egg:#b8d8d6;
    --duck-egg-soft:#eef5f4;
    --teal:#5aaeab;
    --ink:#4a4f55;
    --muted:#8a9096;
    --line:#dfe5e5;
    --white:#ffffff;
    --footer:#3b3e42;
    --footer-deep:#2f3235;
  }
  *{box-sizing:border-box;margin:0;padding:0}
  html,body{width:1200px;height:2996px;overflow:hidden;background:var(--white)}
  body{font-family:"Open Sans",Arial,sans-serif;color:var(--ink);font-size:13px;line-height:1.6}
  .page{position:relative;width:1200px;height:2996px;overflow:hidden}

  /* Hero */
  .hero{position:relative;height:540px;overflow:hidden;color:var(--white)}
  .hero-backdrop{position:absolute;inset:0;background:
    radial-gradient(ellipse 60% 45% at 50% 95%,rgba(255,255,255,.55),transparent 70%),
    radial-gradient(ellipse 35% 30% at 12% 75%,rgba(210,230,250,.55),transparent 70%),
    radial-gradient(ellipse 35% 30% at 88% 75%,rgba(210,230,250,.5),transparent 70%),
    linear-gradient(180deg,var(--hero-deep) 0%,var(--hero-mid) 55%,var(--hero-light) 100%)}
  .site-header{position:absolute;top:0;left:0;right:0;height:96px;display:flex;align-items:center;justify-content:space-between;padding:0 70px 0 86px}
  .brand{display:flex;align-items:center;gap:12px;font-family:"Raleway",sans-serif;font-weight:500;font-size:26px;letter-spacing:2px;color:var(--white)}
  .brand-dot{width:30px;height:30px;border-radius:50%;background:var(--white);opacity:.85}
  .main-nav{display:flex;gap:6px}
  .main-nav a{display:block;border:1px solid rgba(255,255,255,.8);padding:5px 14px;font-family:"Raleway",sans-serif;font-size:13px;color:var(--white);text-decoration:none;background:rgba(255,255,255,.08)}
  .main-nav a.is-active{background:var(--white);color:var(--hero-deep)}
  .hero-copy{position:absolute;top:200px;left:0;right:0;text-align:center;font-family:"Raleway",sans-serif}
  .hero-kicker{font-size:18px;letter-spacing:3px;font-weight:500}
  .hero-title{font-size:72px;font-weight:500;line-height:1.1;margin-top:14px}
  .hero-sub{font-size:20px;font-weight:400;margin-top:14px}
  .btn-book{display:inline-block;margin-top:34px;border:2px solid var(--white);padding:8px 40px;font-size:26px;letter-spacing:1px;color:var(--white);text-decoration:none;font-weight:400}

  /* Intro */
  .intro{height:320px;background:var(--duck-egg);text-align:center;padding:52px 120px 0}
  .section-title{font-family:"Raleway",sans-serif;font-weight:400;font-size:34px;color:var(--white)}
  .intro p{color:#4f6463;font-size:12.5px;margin-top:18px}

  /* Service rows */
  .service-row{display:flex;height:320px}
  .service-media{width:600px;height:320px}
  .service-text{width:600px;padding:44px 60px 0}
  .service-text.tinted{background:var(--duck-egg-soft)}
  .service-title{font-family:"Raleway",sans-serif;font-weight:400;font-size:27px;color:var(--teal);padding-bottom:12px;border-bottom:1px solid var(--line);margin-bottom:16px}
  .service-text p{font-size:12.5px;color:var(--muted);margin-bottom:12px}
  .read-more{display:inline-block;font-size:11px;letter-spacing:2px;color:var(--teal);border-bottom:1px solid var(--teal);text-decoration:none;margin-top:10px}
  .media-mist-blue{background:linear-gradient(135deg,var(--hero-deep),var(--hero-mid) 60%,#c9dcf2)}
  .media-facial{background:linear-gradient(120deg,#f1f3f5,#d9e3ea 55%,#b9c9d6)}
  .media-chamber{background:linear-gradient(120deg,#5b4a3a,#a79a8c 45%,#dcdcdc)}
  .media-mist{background:linear-gradient(120deg,#dff0f6,#b7dff0 50%,#7cc7e4)}

  /* Testimonials */
  .testimonials{height:480px;text-align:center;padding-top:70px}
  .testimonials .section-title{color:var(--teal);font-size:36px}
  .testimonials .lead{color:var(--muted);font-size:12.5px;margin-top:8px}
  .quote-grid{display:flex;justify-content:center;gap:40px;margin-top:46px}
  .quote{width:280px;text-align:left}
  .quote-card{border:1px solid var(--line);padding:22px 22px 22px 40px;font-size:12px;color:var(--muted);position:relative;height:120px}
  .quote-card svg{position:absolute;left:16px;top:24px}
  .quote-author{display:flex;align-items:center;gap:14px;margin-top:22px}
  .avatar{width:50px;height:50px;border-radius:50%;background:var(--duck-egg)}
  .author-name{color:var(--teal);font-size:13px;line-height:1.3}
  .author-role{color:var(--muted);font-size:11px}

  /* Footer */
  .site-footer{height:320px;background:var(--footer);color:#c9ccd0;display:flex;padding:40px 0 0}
  .footer-col{padding:0 50px;border-right:1px solid #55595e;height:240px}
  .footer-col:last-child{border-right:none}
  .col-contact{width:440px;padding-left:110px}
  .col-links{width:380px}
  .col-social{width:380px}
  .footer-brand{display:flex;align-items:center;gap:12px;font-family:"Raleway",sans-serif;font-size:24px;letter-spacing:2px;color:var(--white);margin-bottom:30px}
  .footer-heading{font-size:11px;letter-spacing:2px;color:var(--white);font-weight:600;margin-bottom:14px}
  .contact-line{display:flex;align-items:center;gap:10px;font-size:11.5px;margin-bottom:6px}
  .footer-list{list-style:none}
  .footer-list li{font-size:11.5px;margin-bottom:10px;display:flex;align-items:center;gap:8px}
  .footer-list li::before{content:"›";color:var(--teal)}
  .social-list{list-style:none}
  .social-list li{display:flex;align-items:center;gap:14px;font-size:12px;margin-bottom:14px}
  .social-dot{width:30px;height:30px;border-radius:50%;background:#e4e6e8}
  .copyright{height:56px;background:var(--footer-deep);color:#9ea3a8;font-size:11px;text-align:center;line-height:56px}
</style>
</head>
<body>
<div class="page">

  <section class="hero">
    <div class="hero-backdrop" role="img" aria-label="Swirling cold mist against a deep blue background"></div>
    <header class="site-header">
      <div class="brand"><span class="brand-dot"></span>FROSTWELL</div>
      <nav class="main-nav">
        <a href="#">Home</a>
        <a href="#">Our Services</a>
        <a href="#" class="is-active">About Us</a>
        <a href="#">Price List</a>
        <a href="#">Blog</a>
        <a href="#">Contact Us</a>
      </nav>
    </header>
    <div class="hero-copy">
      <div class="hero-kicker">FROSTWELL STUDIO</div>
      <h1 class="hero-title">Recover Faster With Cold</h1>
      <div class="hero-sub">Whole body, localised and facial treatments</div>
      <a class="btn-book" href="#">BOOK NOW</a>
    </div>
  </section>

  <section class="intro">
    <h2 class="section-title">What is Whole Body Cryotherapy?</h2>
    <p>Whole body cryotherapy exposes the body to extremely cold, dry air for two to three minutes inside a chamber. The rapid drop in skin temperature triggers a natural response that helps reduce inflammation, ease aching muscles and lift energy levels. Many clients use it after training, during recovery or simply to feel sharper and more alert through the working day.</p>
    <p>Sessions are short, dry and supervised by trained staff at every stage. You stay in control throughout, and most people leave feeling refreshed and calm.</p>
  </section>

  <section class="service-row">
    <div class="service-media media-mist-blue" role="img" aria-label="Cold blue mist drifting across the frame"></div>
    <div class="service-text">
      <h3 class="service-title">Whole Body Cryotherapy</h3>
      <p>Short, supervised sessions in extremely cold air help the body recover faster and reduce everyday stiffness. Our team guides you through every step.</p>
      <p>Book a single visit or a package that suits your routine and goals.</p>
      <a class="read-more" href="#">READ MORE</a>
    </div>
  </section>

  <section class="service-row">
    <div class="service-text tinted">
      <h3 class="service-title">Cryofacials</h3>
      <p>A gentle stream of cold vapour tightens the skin, calms redness and leaves the face looking brighter and fresher in under fifteen minutes.</p>
      <p>A quick treatment that fits easily into a lunch break.</p>
      <a class="read-more" href="#">READ MORE</a>
    </div>
    <div class="service-media media-facial" role="img" aria-label="Client receiving a cryofacial treatment"></div>
  </section>

  <section class="service-row">
    <div class="service-media media-chamber" role="img" aria-label="Whole body cryotherapy chamber in the studio"></div>
    <div class="service-text">
      <h3 class="service-title">Localised Cryotherapy</h3>
      <p>Targeted cold is applied to a single joint or muscle group to ease pain and swelling, ideal for sports injuries and areas of ongoing tension.</p>
      <p>Sessions take a few minutes and can be combined with others.</p>
      <a class="read-more" href="#">READ MORE</a>
    </div>
  </section>

  <section class="service-row">
    <div class="service-text tinted">
      <h3 class="service-title">Packages &amp; Memberships</h3>
      <p>Regular sessions bring the best results. Choose a monthly plan that mixes body, local and facial treatments at a lower price per visit.</p>
      <p>Flexible plans with easy online booking at any time.</p>
      <a class="read-more" href="#">READ MORE</a>
    </div>
    <div class="service-media media-mist" role="img" aria-label="Woman surrounded by soft cold mist"></div>
  </section>

  <section class="testimonials">
    <h2 class="section-title">Our Customer Testimonials</h2>
    <p class="lead">Real stories from the people who visit our studio every week.</p>
    <div class="quote-grid">
      <div class="quote">
        <div class="quote-card">
          <svg width="14" height="12" viewBox="0 0 14 12"><path d="M0 12V6l3-6h3L4 6h2v6zM8 12V6l3-6h3l-2 6h2v6z" fill="#b8d8d6"/></svg>
          The staff made me feel at ease from the first visit. I sleep better and recover faster after training.
        </div>
        <div class="quote-author"><span class="avatar"></span><div><div class="author-name">Laura Bennett</div><div class="author-role">Regular Client</div></div></div>
      </div>
      <div class="quote">
        <div class="quote-card">
          <svg width="14" height="12" viewBox="0 0 14 12"><path d="M0 12V6l3-6h3L4 6h2v6zM8 12V6l3-6h3l-2 6h2v6z" fill="#b8d8d6"/></svg>
          A quick session before work keeps my back loose all day. The booking is simple and the team is great.
        </div>
        <div class="quote-author"><span class="avatar"></span><div><div class="author-name">Daniel Hayes</div><div class="author-role">Regular Client</div></div></div>
      </div>
    </div>
  </section>

  <footer class="site-footer">
    <div class="footer-col col-contact">
      <div class="footer-brand"><span class="brand-dot"></span>FROSTWELL</div>
      <div class="footer-heading">OUR CONTACTS</div>
      <div class="contact-line"><svg width="12" height="14" viewBox="0 0 12 14"><path d="M6 0a5 5 0 0 0-5 5c0 4 5 9 5 9s5-5 5-9a5 5 0 0 0-5-5zm0 7a2 2 0 1 1 0-4 2 2 0 0 1 0 4z" fill="#5aaeab"/></svg>12 Harbour Lane, Northgate</div>
      <div class="contact-line"><svg width="12" height="12" viewBox="0 0 12 12"><path d="M2 0l2 3-1 1c1 2 3 4 5 5l1-1 3 2-1 2C5 12 0 7 0 2z" fill="#5aaeab"/></svg>+00 1234 567 890</div>
      <div class="contact-line"><svg width="12" height="10" viewBox="0 0 12 10"><path d="M0 0h12v10H0zM0 0l6 5 6-5" fill="none" stroke="#5aaeab"/></svg>hello@frostwell.example</div>
    </div>
    <div class="footer-col col-links">
      <div class="footer-heading">USEFUL LINKS</div>
      <ul class="footer-list">
        <li>Home</li><li>Our Services</li><li>About Us</li><li>Price List</li><li>Blog</li><li>Contact Us</li>
      </ul>
    </div>
    <div class="footer-col col-social">
      <div class="footer-heading">SOCIAL LINKS</div>
      <ul class="social-list">
        <li><span class="social-dot"></span>Community</li>
        <li><span class="social-dot"></span>Updates</li>
        <li><span class="social-dot"></span>Circle</li>
        <li><span class="social-dot"></span>Network</li>
      </ul>
    </div>
  </footer>
  <div class="copyright">Copyright © 2024 All Rights Reserved | Terms Of Use | Privacy Policy</div>

</div>
</body>
</html>
```